Insight Plus. needs Business Cards

For this project, we need business cards (currently have also put a call out for a logo). We are a start-up called Insight Plus. This is our second company (our first one was called Querivance). Traditionally we have been providing market research services across different sectors, primarily financial services and the pharmaceutical industry. However, we now want to go beyond market research to offer more (Plus.)... strategic consulting and big data knowledge management. We want our brand to be approachable, creative, fun but professional.

Target Market(s)

The target audience is a business professional - we are B2B (business to business) and do not sell our services to individuals. The brands we work with are major brands across industries, but primarily automotive, financial and pharmaceutical.

Industry/Entity Type

Market Research

Font styles to use
Serif
Sans Serif
Other font styles liked:
• Calibri

Requirements
Must have
• Be clean, simple, modern
Show our address and phone number and email address and website URL
We do not need to have titles showing.

```html
<!DOCTYPE html>
<html lang="en">
<head>
<meta charset="utf-8">
<title>Insight Plus. Business Cards</title>
<link href="https://fonts.googleapis.com/css2?family=Open+Sans:wght@400;600&display=swap" rel="stylesheet">
<style>
  :root {
    --stage: #e9e6e1;
    --card-white: #f7f7f7;
    --card-black: #151515;
    --band-black: #1c1c1c;
    --ink: #3a3a3a;
    --ink-soft: #5a5a5a;
    --accent-blue: #2fa3dc;
    --brand-light: #d9d9d9;
    --divider: #b9b9b9;
    --shadow: rgba(0,0,0,0.25);
  }
  html, body {
    margin: 0;
    padding: 0;
    width: 1200px;
    height: 1023px;
    overflow: hidden;
    background: var(--stage);
    font-family: "Open Sans", Calibri, sans-serif;
  }
  .canvas {
    position: relative;
    width: 1200px;
    height: 1023px;
  }
  .card {
    position: absolute;
    width: 588px;
    height: 336px;
    border-radius: 4px;
    box-shadow: 0 10px 30px var(--shadow);
    overflow: hidden;
  }
  /* Front card */
  .card-front {
    left: 90px;
    top: 110px;
    background: var(--card-white);
  }
  .brand-band {
    height: 86px;
    background: linear-gradient(180deg, #2a2a2a, var(--band-black));
    display: flex;
    align-items: center;
    padding-left: 36px;
  }
  .brand-name {
    font-weight: 600;
    font-size: 34px;
    letter-spacing: 8px;
    color: var(--brand-light);
    text-transform: uppercase;
  }
  .front-body {
    position: relative;
    height: 250px;
  }
  .person {
    position: absolute;
    left: 36px;
    top: 30px;
  }
  .person-name {
    font-size: 24px;
    color: var(--accent-blue);
    letter-spacing: 1px;
    text-transform: uppercase;
    margin: 0;
    font-weight: 400;
  }
  .person-role {
    font-size: 14px;
    color: var(--ink-soft);
    margin: 2px 0 0;
  }
  .contact-list {
    position: absolute;
    left: 36px;
    top: 118px;
    list-style: none;
    margin: 0;
    padding: 0;
  }
  .contact-list li {
    display: flex;
    align-items: center;
    gap: 10px;
    font-size: 13.5px;
    color: var(--ink);
    line-height: 22px;
  }
  .contact-icon {
    width: 12px;
    height: 12px;
    border-radius: 2px;
    background: var(--accent-blue);
    flex: none;
  }
  .column-divider {
    position: absolute;
    left: 318px;
    top: 0;
    width: 1px;
    height: 250px;
    background: var(--divider);
  }
  .address {
    position: absolute;
    left: 344px;
    top: 118px;
    font-style: normal;
    font-size: 13.5px;
    line-height: 22px;
    color: var(--ink);
  }
  .address-company {
    color: var(--accent-blue);
    font-weight: 600;
  }
  .corner-mark {
    position: absolute;
    right: 34px;
    top: 30px;
    width: 40px;
    height: 40px;
    background: #8fc46a;
    opacity: 0.7;
  }
  /* Back card */
  .card-back {
    left: 540px;
    top: 560px;
    background: radial-gradient(ellipse at 40% 30%, #2a2a2a, var(--card-black) 70%);
  }
  .back-content {
    position: absolute;
    inset: 0;
    display: flex;
    flex-direction: column;
    align-items: center;
    justify-content: center;
    gap: 6px;
  }
  .back-brand {
    font-weight: 600;
    font-size: 38px;
    letter-spacing: 6px;
    color: #ffffff;
    text-transform: uppercase;
  }
  .back-url {
    font-size: 16px;
    color: #e0e0e0;
    letter-spacing: 1.5px;
  }
</style>
</head>
<body>
<main class="canvas">
  <section class="card card-front" aria-label="Business card front">
    <header class="brand-band">
      <span class="brand-name">Insight Plus.</span>
    </header>
    <div class="front-body">
      <div class="person">
        <h1 class="person-name">Daniel Keller</h1>
        <p class="person-role">General Director</p>
      </div>
      <ul class="contact-list">
        <li><span class="contact-icon"></span>800.555.0142</li>
        <li><span class="contact-icon"></span>800.555.0187</li>
        <li><span class="contact-icon"></span>0123.555.010</li>
        <li><span class="contact-icon"></span>daniel@insightplus.com</li>
        <li><span class="contact-icon"></span>www.insightplus.com</li>
      </ul>
      <div class="column-divider"></div>
      <address class="address">
        <div class="address-company">Insight Plus.</div>
        740 Lakeside Ave NE<br>
        Suite 210, Building C<br>
        Kirkland, Washington<br>
        USA 98033
      </address>
      <div class="corner-mark"></div>
    </div>
  </section>

  <section class="card card-back" aria-label="Business card back">
    <div class="back-content">
      <span class="back-brand">Insight Plus.</span>
      <span class="back-url">www.insightplus.com</span>
    </div>
  </section>
</main>
</body>
</html>
```